Medical Centre Trifold Brochure

New Medical Centre needs a bright and airy Trifold brochure. We want to introduce our practice to the surrounding area so want to advise our services and introduce the Doctors and Nurses.

I will upload all the pictures and logos, along with some pdf pages of styles that we like (and some we dont) to assist your creativity.

We will provide as much feedback for you as possible.

After this project, we would like to work with the same designer to expand into some other brochures etc that we have in mind, so this is a starting point.

Hi Designers,

We are looking forward to seeing yuor work. Are you happy that you have enough information to get started?

Please let me know if you need anything else?

Cheers

Hi Designers.. I should mention the brochure itself.. we are looking for a doubled sided, full colour brochure that will be folded into thirds so it becomes a DL size.. I hope that makes sense.

Any questions always welcome.

Target Market(s)

Females - Mothers / Wives / Grandmothers

Industry/Entity Type

Medical

Requirements
Must have
• Tri Fold Medical – Larkvale Family Health

• Include images of the Doctors (I will supply) and the Nursing Staff

• “Chunks” of information
o Introduction to who we are (I will supply)
o Our services (I will supply)
o Fee’s
• We are a newly renovated Medical Clinic
• Plotwise Map of our location – Photo of the outside of the centre near the plotwise map
• Opening Hours
• Contact Details / website address www.larkvalefamilyhealth.com.au (not yet live but must be included)
• Interior Reception area photo
• Ask a question.. “Are you worried about your patient history?.. We can help”
• Need to leave a space for a Magnet.. (business card sized)

3 Doctor Photos (2 uploaded already)
Image of the centre (uploaded already)

I will upload a detailed description of what we are looking for.
Nice to have
• Photo's of 2 Nurses (1 already uploaded - Maren)

```html
<!DOCTYPE html>
<html lang="en">
<head>
<meta charset="utf-8">
<title>Larkvale Family Health – Trifold Brochure</title>
<link href="https://fonts.googleapis.com/css2?family=Questrial&family=Arimo:wght@400;700&display=swap" rel="stylesheet">
<style>
  :root {
    --green: #8cc63e;
    --green-soft: #9ed04f;
    --grey: #5b5e61;
    --grey-light: #8a8d90;
    --white: #ffffff;
    --card-text: #e4e5e6;
    --accent-yellow: #f4ec6a;
    --page: #ecebe8;
  }
  * { box-sizing: border-box; margin: 0; padding: 0; }
  html, body { width: 900px; height: 1200px; overflow: hidden; }
  body {
    background: var(--page);
    font-family: "Arimo", Arial, sans-serif;
    color: var(--white);
    position: relative;
  }
  .brochure-side {
    position: absolute;
    left: 75px;
    width: 750px;
    height: 530px;
    overflow: hidden;
    box-shadow: 0 2px 8px rgba(0,0,0,.18);
  }
  .side-outer { top: 50px; }
  .side-inner { top: 616px; }
  .side-art { position: absolute; inset: 0; }
  .block { position: absolute; }
  .section-title {
    font-family: "Questrial", "Arimo", sans-serif;
    font-size: 21px; font-weight: 400; letter-spacing: .3px; line-height: 1.1;
  }

  /* Outer side */
  .brand {
    left: 532px; top: 70px; width: 200px;
    display: flex; align-items: center; gap: 10px;
    color: var(--green);
  }
  .brand-mark { width: 20px; height: 20px; background: var(--green); flex: none; }
  .brand-name {
    font-family: "Questrial", "Arimo", sans-serif;
    font-size: 22px; line-height: 1.1; font-weight: 400;
  }

  .doctor-card {
    left: 18px; width: 230px; height: 80px;
    background: var(--grey);
    border-radius: 8px;
    display: flex; gap: 9px; padding: 6px;
  }
  .doctor-card.c1 { top: 212px; }
  .doctor-card.c2 { top: 312px; }
  .doctor-card.c3 { top: 410px; }
  .doctor-photo {
    width: 66px; height: 68px; flex: none;
    background: linear-gradient(160deg, #f2efe9, #cfc8bd);
    border-radius: 3px;
  }
  .doctor-text { min-width: 0; }
  .doctor-name {
    font-family: "Questrial", "Arimo", sans-serif;
    font-size: 15px; font-weight: 400; white-space: nowrap;
    margin: 3px 0 5px;
  }
  .doctor-bio { font-size: 6.8px; line-height: 1.35; color: var(--card-text); }

  .position { left: 277px; top: 204px; width: 180px; }
  .map-area {
    left: 277px; top: 238px; width: 154px; height: 90px;
    background: linear-gradient(135deg, #eeeae0, #d9d6cc);
    border: 1px solid #cfcfcf;
  }
  .contact {
    left: 277px; top: 342px; width: 190px;
    font-size: 8.3px; line-height: 1.42; font-style: normal;
  }
  .hours { left: 277px; top: 432px; width: 190px; }
  .hours-list { font-size: 8.8px; line-height: 1.5; margin-top: 5px; }
  .web-strip {
    right: 12px; bottom: 6px; font-size: 8.5px; font-weight: 700;
  }

  /* Inner side */
  .about { left: 20px; top: 22px; width: 218px; }
  .about .section-title { margin-bottom: 9px; }
  .body-copy { font-size: 9.2px; line-height: 1.34; text-align: justify; }
  .services { left: 268px; top: 240px; width: 222px; }
  .fees { left: 520px; top: 240px; width: 215px; }
  .services .section-title, .fees .section-title { margin-bottom: 7px; }
  .service-list {
    list-style: none; margin-top: 12px;
    font-size: 9.2px; line-height: 1.45; color: var(--accent-yellow);
  }
  .service-list li::before { content: "•"; margin-right: 6px; }
</style>
</head>
<body>

<section class="brochure-side side-outer">
  <svg class="side-art" width="750" height="530" viewBox="0 0 750 530">
    <defs>
      <linearGradient id="gBuilding" x1="0" y1="0" x2="0" y2="1">
        <stop offset="0" stop-color="#9fb9dc"/>
        <stop offset=".45" stop-color="#c7b2a2"/>
        <stop offset="1" stop-color="#9c6a55"/>
      </linearGradient>
      <linearGradient id="gFamily" x1="0" y1="0" x2="1" y2="1">
        <stop offset="0" stop-color="#cfe3f2"/>
        <stop offset=".6" stop-color="#e9d6c7"/>
        <stop offset="1" stop-color="#8fb4d6"/>
      </linearGradient>
    </defs>
    <rect width="750" height="530" fill="var(--green)"/>
    <rect x="500" y="0" width="250" height="215" fill="var(--white)"/>
    <rect x="0" y="0" width="500" height="178" fill="url(#gBuilding)" role="img" aria-label="Photo of the renovated medical centre building exterior"/>
    <path d="M0 168 C180 150 380 152 520 190 L750 190 L750 214 L520 214 C380 178 180 176 0 198 Z" fill="var(--grey)"/>
    <path d="M750 232 C640 252 560 300 500 400 C472 450 462 500 456 530 H750 Z" fill="url(#gFamily)" role="img" aria-label="Photo of a smiling family outdoors"/>
    <path d="M750 222 C636 244 552 292 490 396 C462 446 450 500 444 530" fill="none" stroke="var(--grey)" stroke-width="16"/>
    <rect x="456" y="508" width="294" height="22" fill="var(--grey)"/>
  </svg>

  <div class="block brand">
    <span class="brand-mark"></span>
    <span class="brand-name">Larkvale Family Health</span>
  </div>

  <article class="block doctor-card c1">
    <div class="doctor-photo" role="img" aria-label="Portrait of Dr. Priya"></div>
    <div class="doctor-text">
      <h3 class="doctor-name">Dr. Priya</h3>
      <p class="doctor-bio">General practitioner with a gentle, family focused approach to care for women, children and older patients.</p>
    </div>
  </article>
  <article class="block doctor-card c2">
    <div class="doctor-photo" role="img" aria-label="Portrait of Dr. Maren"></div>
    <div class="doctor-text">
      <h3 class="doctor-name">Dr. Maren</h3>
      <p class="doctor-bio">Experienced doctor caring for whole families, with a keen interest in women's health and preventive checks.</p>
    </div>
  </article>
  <article class="block doctor-card c3">
    <div class="doctor-photo" role="img" aria-label="Portrait of Dr. Owen Hartley"></div>
    <div class="doctor-text">
      <h3 class="doctor-name">Dr. Owen Hartley</h3>
      <p class="doctor-bio">Long serving local GP offering care plans, health assessments and friendly advice for every age group.</p>
    </div>
  </article>

  <div class="block position"><h2 class="section-title">POSITION</h2></div>
  <div class="block map-area" role="img" aria-label="Plotwise map of the centre location"></div>
  <address class="block contact">
    4/118 Fernbrook Rd, Larkvale<br>
    SA 5999, Australia<br>
    P : (08) 5550 1441<br>
    F : (08) 5550 1434<br>
    E : info@larkvalefamilyhealth.com.au<br>
    W : www.larkvalefamilyhealth.com.au
  </address>
  <div class="block hours">
    <h2 class="section-title">Opening Hour</h2>
    <p class="hours-list">Mon - Fri : 08.00AM - 08.00PM<br>Sat - Sun : 10.00AM - 10.30PM</p>
  </div>
  <div class="block web-strip">www.larkvalefamilyhealth.com.au</div>
</section>

<section class="brochure-side side-inner">
  <svg class="side-art" width="750" height="530" viewBox="0 0 750 530">
    <defs>
      <linearGradient id="gKids" x1="0" y1="0" x2="1" y2="1">
        <stop offset="0" stop-color="#6fb1e6"/>
        <stop offset=".6" stop-color="#e8a15a"/>
        <stop offset="1" stop-color="#5d9b3c"/>
      </linearGradient>
      <linearGradient id="gCouple" x1="0" y1="0" x2="1" y2="1">
        <stop offset="0" stop-color="#7aa85a"/>
        <stop offset=".5" stop-color="#e6cdb7"/>
        <stop offset="1" stop-color="#9a86c2"/>
      </linearGradient>
      <linearGradient id="gStaff" x1="0" y1="0" x2="0" y2="1">
        <stop offset="0" stop-color="#ffffff"/>
        <stop offset=".5" stop-color="#c9d8e8"/>
        <stop offset="1" stop-color="#6d8fb5"/>
      </linearGradient>
      <linearGradient id="gTeens" x1="0" y1="0" x2="1" y2="1">
        <stop offset="0" stop-color="#f0e2d4"/>
        <stop offset="1" stop-color="#c9866a"/>
      </linearGradient>
    </defs>
    <rect width="750" height="530" fill="var(--green)"/>
    <path d="M250 0 H485 V168 C400 166 320 178 250 200 Z" fill="url(#gKids)" role="img" aria-label="Photo of children playing outdoors"/>
    <path d="M485 0 H750 V252 C650 204 560 176 485 168 Z" fill="url(#gCouple)" role="img" aria-label="Photo of a smiling senior couple"/>
    <path d="M250 204 C410 150 600 168 750 262" fill="none" stroke="var(--grey)" stroke-width="22"/>
    <path d="M0 268 C90 252 180 236 250 204 V530 H0 Z" fill="url(#gStaff)" role="img" aria-label="Photo of the doctors and nursing team"/>
    <rect x="522" y="392" width="228" height="138" fill="url(#gTeens)" role="img" aria-label="Photo of a group of smiling teenagers"/>
  </svg>

  <div class="block about">
    <h2 class="section-title">ABOUT US</h2>
    <p class="body-copy">Lorem ipsum dolor sit amet, consectetur adipisicing elit, sed do eiusmod tempor incididunt ut labore et dolore magna aliqua. Ut enim ad minim veniam, quis nostrud exercitation ullamco laboris nisi ut aliquip ex ea commodo consequat. Duis aute irure dolor in reprehenderit in voluptate velit esse cillum dolore eu fugiat nulla pariatur. Excepteur sint occaecat cupidatat non proident, sunt in culpa qui officia deserunt mollit anim id est laborum.</p>
  </div>

  <div class="block services">
    <h2 class="section-title">SERVICES</h2>
    <p class="body-copy">Lorem ipsum dolor sit amet, consectetur adipisicing elit, sed do eiusmod tempor incididunt ut labore et dolore</p>
    <ul class="service-list">
      <li>Medical – Larkvale Family Health</li>
      <li>Dental - Larkvale Family Dental</li>
      <li>Physiotherapy (we say "Physio")</li>
      <li>Podiatry</li>
      <li>Psychology</li>
      <li>Dieticians</li>
    </ul>
  </div>

  <div class="block fees">
    <h2 class="section-title">FEE'S</h2>
    <p class="body-copy">Lorem ipsum dolor sit amet, consectetur adipisicing elit, sed do eiusmod tempor incididunt ut labore et dolore magna aliqua. Ut enim ad minim veniam, quis nostrud exercitation ullamco laboris nisi ut aliquip ex ea commodo consequat. Duis aute irure dolor in reprehenderit in voluptate velit esse</p>
  </div>
</section>

</body>
</html>
```